Business card design needed

It's a new business in town.Something so the name stands out.I need a logo for the B.R.W
I may all so use the design as a sign on a building

Contact Information for Business Card

B.R.W
Brindlewood Auto Detailing
42 Fenwarra Crs
Brindlewood Vic 3799
Ph:(03)59284736
Mob:0417362958

```html
<!DOCTYPE html>
<html lang="en">
<head>
<meta charset="utf-8">
<title>B.R.W Brindlewood Auto Detailing – Business Card</title>
<link rel="stylesheet" href="https://fonts.googleapis.com/css2?family=Open+Sans:wght@400;600;700;800&display=swap">
<style>
  :root {
    --backdrop: #1d1d1f;
    --card-blue: #3fb8e0;
    --band-white: #ffffff;
    --ink-dark: #111418;
    --text-light: #ffffff;
    --mark-navy: #14181d;
  }
  * { margin: 0; padding: 0; box-sizing: border-box; }
  html, body {
    width: 1200px;
    height: 900px;
    overflow: hidden;
    background: var(--backdrop);
    font-family: "Open Sans", Arial, sans-serif;
  }
  .stage {
    position: relative;
    width: 1200px;
    height: 900px;
  }
  .business-card {
    position: absolute;
    left: 150px;
    top: 193px;
    width: 900px;
    height: 514px;
    background: var(--card-blue);
    border-radius: 16px;
    overflow: hidden;
  }
  .brand-square {
    position: absolute;
    left: 44px;
    top: 42px;
    width: 128px;
    height: 128px;
    background: var(--mark-navy);
  }
  .brand-name {
    position: absolute;
    left: 194px;
    top: 92px;
    font-size: 60px;
    font-weight: 700;
    letter-spacing: 1px;
    color: var(--text-light);
    line-height: 1;
  }
  .info-band {
    position: absolute;
    left: 0;
    top: 216px;
    width: 843px;
    height: 79px;
    background: var(--band-white);
  }
  .address {
    position: absolute;
    left: 57px;
    top: 12px;
    font-size: 20px;
    font-weight: 700;
    line-height: 31px;
    color: var(--ink-dark);
  }
  .contacts {
    position: absolute;
    right: 40px;
    top: 12px;
    font-size: 20px;
    font-weight: 700;
    line-height: 31px;
    color: var(--ink-dark);
  }
  .contact-row {
    display: flex;
    align-items: center;
    justify-content: flex-end;
    gap: 30px;
  }
  .contact-icon {
    width: 18px;
    height: 20px;
    flex: none;
  }
  .contact-number { min-width: 150px; text-align: right; }
  .business-title {
    position: absolute;
    left: 59px;
    top: 393px;
    font-size: 27px;
    font-weight: 700;
    color: var(--text-light);
    line-height: 1;
  }
  .business-subtitle {
    position: absolute;
    left: 147px;
    top: 428px;
    font-size: 22px;
    font-weight: 600;
    color: var(--text-light);
    line-height: 1;
  }
</style>
</head>
<body>
<main class="stage">
  <article class="business-card">
    <div class="brand-square" aria-hidden="true"></div>
    <h1 class="brand-name">B.R.W</h1>

    <section class="info-band">
      <address class="address" style="font-style:normal">
        42 Fenwarra Crs<br>
        Brindlewood Vic 3799
      </address>
      <div class="contacts">
        <div class="contact-row">
          <svg class="contact-icon" viewBox="0 0 18 20" aria-label="Phone">
            <path d="M2 6 C2 3 5 2 9 2 C13 2 16 3 16 6 L13 7 L12 5 L6 5 L5 7 Z" fill="#111418"/>
            <rect x="3" y="9" width="12" height="9" rx="1.5" fill="#111418"/>
            <circle cx="9" cy="13.5" r="2.2" fill="#ffffff"/>
          </svg>
          <span class="contact-number">(03)59284736</span>
        </div>
        <div class="contact-row">
          <svg class="contact-icon" viewBox="0 0 18 20" aria-label="Mobile">
            <rect x="4" y="1" width="10" height="18" rx="2" fill="#111418"/>
            <rect x="6" y="4" width="6" height="7" fill="#ffffff"/>
            <circle cx="9" cy="15" r="1.4" fill="#ffffff"/>
          </svg>
          <span class="contact-number">0417362958</span>
        </div>
      </div>
    </section>

    <p class="business-title">B.R.W Brindlewood</p>
    <p class="business-subtitle">Auto Detailing</p>
  </article>
</main>
</body>
</html>
```